Web Site Design

We need to design the whole web site for our small start up. We sell hospitality and culinary art internships abroad. I did my own design with WIX which is horrible meanwhile I started with my business. You can see it www.brindle-passage.org I will need you to create a new and attractive web site and to leave it working on wix. The internship destinations are United Arab Emirates, Thailand, China, Spain, Brazil and maybe leave a couple of pages for future destinations.You could also get other ideas of other sites that do internships.

Target Market(s)

Students and recent graduates of hospitality and culinary art majors

Industry/Entity Type

Education

Number of Pages Required

5+ page

Requirements
Must have
• Addittional to our program destinations, or to the pages in the current site. The website must contain a page for Universities or Hotels who require our service

```html
<!DOCTYPE html>
<html lang="en">
<head>
<meta charset="utf-8">
<title>Brindle Passage – Hospitality &amp; Culinary Art Internships Abroad</title>
<link href="https://fonts.googleapis.com/css2?family=Montserrat:wght@300;400;500;600;700&display=swap" rel="stylesheet">
<style>
  :root{
    --accent:#f9b940;
    --accent-soft:#fcc860;
    --ink:#555555;
    --ink-soft:#8a8a8a;
    --ink-faint:#a3a3a3;
    --white:#ffffff;
    --rule:#e6e6e6;
  }
  *{box-sizing:border-box;margin:0;padding:0}
  html,body{width:950px;height:1200px;overflow:hidden;background:var(--white)}
  body{font-family:'Montserrat',sans-serif;color:var(--ink);position:relative}
  .accent{color:var(--accent)}

  /* Hero */
  .hero{position:absolute;left:0;top:0;width:950px;height:372px;
    background:radial-gradient(ellipse at 55% 40%,#6b5a4a 0%,#3b3028 45%,#1f1a16 100%)}
  .nav{position:absolute;top:17px;left:212px;right:212px;display:flex;align-items:center;justify-content:space-between}
  .brand{font-size:16px;font-weight:600;color:var(--accent)}
  .hero .brand{color:var(--accent)}
  .nav-links{display:flex;gap:23px;list-style:none}
  .nav-links li{font-size:11.5px;font-weight:500;color:var(--white)}
  .nav-links li.active{color:var(--accent);font-weight:600}
  .hero-title{position:absolute;top:108px;width:100%;text-align:center;color:var(--white);font-size:14px;font-weight:600}
  .hero-rule{position:absolute;top:130px;left:453px;width:56px;height:2px;background:var(--accent)}
  .hero-lead{position:absolute;top:141px;width:100%;text-align:center;color:var(--white);font-size:12px;line-height:13px;font-weight:400}
  .search{position:absolute;top:200px;left:284px;width:396px;height:28px;background:rgba(235,235,235,.92);border-radius:2px;display:flex;align-items:center}
  .search span{flex:1;padding-left:11px;font-size:11.5px;color:#777}
  .search-btn{width:22px;height:22px;margin-right:3px;background:var(--accent);border-radius:2px;display:flex;align-items:center;justify-content:center}

  /* Destination */
  .destination{position:absolute;top:372px;left:0;width:950px;height:200px;border-bottom:1px solid var(--rule)}
  .destination h2{position:absolute;top:12px;left:0;width:950px;text-align:center;font-size:13.5px;font-weight:600;color:var(--ink)}
  .dest-photo{position:absolute;top:43px;left:221px;width:170px;height:113px;
    background:linear-gradient(180deg,#a9cde6 0%,#6f9cc0 45%,#2e4f6e 70%,#223b52 100%)}
  .dest-copy{position:absolute;top:41px;left:411px;width:326px;font-size:8.3px;line-height:12.5px;color:var(--ink-faint);font-weight:400}
  .dest-actions{position:absolute;top:159px;left:411px;display:flex;gap:7px}
  .btn{height:22px;width:77px;font-size:10.5px;display:flex;align-items:center;justify-content:center;border-radius:2px}
  .btn-fill{background:var(--accent-soft);color:var(--white)}
  .btn-line{border:1px solid var(--accent);color:var(--ink);width:79px}

  /* Details */
  .details{position:absolute;top:573px;left:0;width:950px;height:316px}
  .col{position:absolute;top:0}
  .col h3{font-size:12px;font-weight:500;color:var(--ink);margin-top:8px;margin-bottom:14px}
  .list{list-style:none}
  .list li{display:flex;align-items:flex-start;gap:6px;font-size:8.3px;line-height:12.5px;color:var(--ink-soft);margin-bottom:12.5px}
  .list li svg{flex:none;margin-top:-1px}
  .list b{font-weight:600;color:var(--ink)}
  .list .strong{color:var(--ink)}
  .col-positions{left:231px}
  .col-positions h3{padding-left:15px}
  .col-duration{left:427px}
  .col-duration h3{padding-left:20px}
  .col-benefits{left:622px;width:200px}
  .col-benefits h3{padding-left:18px;margin-bottom:6px}
  .col-benefits .list li{margin-bottom:12px}

  /* Apply */
  .apply{position:absolute;top:889px;left:0;width:950px;height:195px;
    background:linear-gradient(180deg,#948c7e 0%,#857d6e 55%,#6f685b 100%)}
  .apply h2{position:absolute;top:35px;width:100%;text-align:center;color:var(--white);font-size:14px;font-weight:600}
  .apply p{position:absolute;top:62px;left:355px;width:240px;text-align:center;color:#ece8df;font-size:10.5px;line-height:12.5px}
  .apply-form{position:absolute;top:118px;left:262px;display:flex;gap:14px}
  .field{width:106px;height:26px;background:#f4f4f4;border:1px solid #ddd;font-size:10.5px;color:#aaa;padding:6px 3px}
  .field.wide{width:106px}
  .btn-apply{width:78px;height:26px;background:var(--accent-soft);color:var(--white);font-size:11.5px;font-weight:600;display:flex;align-items:center;justify-content:center;margin-left:-1px}

  /* Footer */
  .footer{position:absolute;top:1084px;left:0;width:950px;height:116px}
  .footer .brand{position:absolute;top:22px;left:212px;font-size:15px;color:var(--accent)}
  .copyright{position:absolute;top:60px;left:213px;font-size:6.5px;color:var(--ink)}
  .fcol{position:absolute;top:27px}
  .fcol h4{font-size:10.5px;font-weight:500;color:var(--accent);margin-bottom:8px}
  .fcol ul{list-style:none}
  .fcol li{font-size:8.3px;color:var(--ink);line-height:14.5px}
  .fcol-links{left:420px}
  .fcol-info{left:527px}
  .fcol-social{left:646px}
  .social{display:flex;gap:7px;margin-top:2px}
  .social span{width:11px;height:11px;border-radius:50%;background:#8a8f98}
</style>
</head>
<body>

<header class="hero" role="img" aria-label="Photo of a barista pouring coffee behind a busy café counter">
  <nav class="nav">
    <div class="brand">Brindle Passage</div>
    <ul class="nav-links">
      <li class="active">Home</li>
      <li>Destinations</li>
      <li>About Us</li>
      <li>Contact Us</li>
    </ul>
  </nav>
  <h1 class="hero-title">Hospitality &amp; Culinary Art Internships <span class="accent">Abroad.</span></h1>
  <div class="hero-rule"></div>
  <p class="hero-lead">Lorem ipsum dolor sit amet, consectetur adipiscing<br>elit. Mauris lobortis tincidunt justo ac dapibus.</p>
  <div class="search">
    <span>Search for internship...</span>
    <div class="search-btn">
      <svg width="12" height="12" viewBox="0 0 12 12"><circle cx="5" cy="5" r="3.8" fill="none" stroke="#fff" stroke-width="1.2"/><line x1="7.8" y1="7.8" x2="11" y2="11" stroke="#fff" stroke-width="1.3"/></svg>
    </div>
  </div>
</header>

<section class="destination">
  <h2>Brazil<span class="accent">.</span></h2>
  <div class="dest-photo" role="img" aria-label="Aerial photo of a coastal city with mountains and a bay in Brazil"></div>
  <p class="dest-copy">Lorem ipsum dolor sit amet, consectetur adipiscing elit. Mauris lobortis tincidunt justo ac dapibus. Vestibulum ante ipsum primis in faucibus orci luctus et ultrices posuere cubilia Curae; Suspendisse sed accumsan mi. Duis volutpat condimentum fermentum. Duis consequat sapien id eleifend faucibus. Pellentesque habitant morbi tristique senectus et netus et malesuada fames ac turpis egestas. Nulla facilisi. Aenean a rhoncus diam, vitae rutrum ex. Sed et leo egestas mi faucibus congue sit amet id ligula. Proin auctor quam sit amet nisl molestie, quis pulvinar metus porttitor. Nulla facilisi. Proin tincidunt tellus id felis dignissim condimentum</p>
  <div class="dest-actions">
    <div class="btn btn-fill">Process</div>
    <div class="btn btn-line">Payment</div>
  </div>
</section>

<svg width="0" height="0" style="position:absolute">
  <defs>
    <symbol id="tick" viewBox="0 0 13 13"><circle cx="6.5" cy="6.5" r="6.5" fill="#f9b940"/><path d="M3.6 6.7l2 2 3.8-4" fill="none" stroke="#fff" stroke-width="1.4"/></symbol>
  </defs>
</svg>

<section class="details">
  <div class="col col-positions">
    <h3>Possible Positions</h3>
    <ul class="list">
      <li><svg width="12" height="12"><use href="#tick"/></svg>Food &amp; Beverage</li>
      <li><svg width="12" height="12"><use href="#tick"/></svg>Guest Services</li>
      <li><svg width="12" height="12"><use href="#tick"/></svg>Front Desk</li>
      <li><svg width="12" height="12"><use href="#tick"/></svg>Manager in Training</li>
      <li><svg width="12" height="12"><use href="#tick"/></svg>...and more!</li>
    </ul>
  </div>
  <div class="col col-duration">
    <h3>Duration</h3>
    <ul class="list">
      <li><svg width="14" height="14" viewBox="0 0 14 14"><circle cx="7" cy="7" r="6" fill="none" stroke="#f9b940" stroke-width="1"/><path d="M7 3.5V7h2.5" fill="none" stroke="#f9b940" stroke-width="1"/></svg>6 Months</li>
    </ul>
  </div>
  <div class="col col-benefits">
    <h3>Benefit Package</h3>
    <ul class="list">
      <li><svg width="12" height="12"><use href="#tick"/></svg><span><span class="strong">Guaranteed Position.</span><br>We guarantee that we will find a position for you based on your experience, goals, and availability...<span class="strong">OR YOUR MONEY BACK</span></span></li>
      <li><svg width="12" height="12"><use href="#tick"/></svg><span class="strong">Monthly Stippen 400$</span></li>
      <li><svg width="12" height="12"><use href="#tick"/></svg><span><span class="strong">Free accommodation</span> provided by the hotel either inside the actual hotel or in an apartment nearby</span></li>
      <li><svg width="12" height="12"><use href="#tick"/></svg><span class="strong">Working meals</span></li>
      <li><svg width="12" height="12"><use href="#tick"/></svg><span class="strong">Wayfarer guide</span></li>
      <li><svg width="12" height="12"><use href="#tick"/></svg><span class="strong">Airport pickup</span></li>
      <li><svg width="12" height="12"><use href="#tick"/></svg><span class="strong">Invitation Letter for visa procedure.</span></li>
      <li><svg width="12" height="12"><use href="#tick"/></svg><span class="strong"><b>US$ 1500 Scholarship</b> to study Chinese with our partner school during your internship program.</span></li>
    </ul>
  </div>
</section>

<section class="apply" role="img" aria-label="Misty landscape of temples with hot air balloons at sunrise">
  <h2>Apply for Internship <span class="accent">Now.</span></h2>
  <p>Lorem ipsum dolor sit amet, consectetur adipiscing elit. Mauris lobortis tincidunt justo ac dapibus.</p>
  <div class="apply-form">
    <div class="field">Name</div>
    <div class="field">Email</div>
    <div class="field wide">Phone Number</div>
    <div class="btn-apply">Apply</div>
  </div>
</section>

<footer class="footer">
  <div class="brand">Brindle Passage</div>
  <div class="copyright">© 2018 Brindle Passage.</div>
  <div class="fcol fcol-links">
    <h4>Links</h4>
    <ul><li>Home</li><li>Destinations</li><li>About Us</li><li>Contact Us</li></ul>
  </div>
  <div class="fcol fcol-info">
    <h4>Info</h4>
    <ul><li>Privacy Policy</li><li>Disclaimer</li><li>Terms &amp; Conditions</li><li>Help</li></ul>
  </div>
  <div class="fcol fcol-social">
    <h4>Social</h4>
    <div class="social"><span></span><span></span><span></span></div>
  </div>
</footer>

</body>
</html>
```